CG 1 page flyer

I need a flyer design for a financial risk advisory business. I like the layout of the example on your site, for Delia Fenwick (attached). Our business needs to show strength, safety, knowledge and security. We provide financial advice.

I have uploaded the front page of our larger brochure. I would like the man with the umbrella with the caption and the logo / brand on the front page, but with portrait orientation, instead of landscape.

For the second page (the back), I have got some ideas of the kinds of things I would want written on the attached Power Point. But it needs to be arranged better, with perhaps the Corvin's Gate Logo on there as well, to break up all the writing. Attached is an example of how it might look, but I want different formatting and layout ideas, that look better, more professional etc.

The page 1 comment what is corvins gate? predicting ......... would look better all the way along the bottom of the page, but i couldn't get the formatting right.

```html
<!DOCTYPE html>
<html lang="en">
<head>
<meta charset="utf-8">
<title>Corvin's Gate – Flyer</title>
<link href="https://fonts.googleapis.com/css2?family=Raleway:wght@300;400;600;700&family=PT+Sans:wght@400;700&display=swap" rel="stylesheet">
<style>
  :root {
    --sky: #3db8ea;
    --sky-soft: #6ccaf0;
    --slate: #58595b;
    --mist: #e6e7e8;
    --paper: #ffffff;
    --ink: #231f20;
    --navy: #2b2f6e;
    --backdrop: #efede9;
  }
  * { box-sizing: border-box; margin: 0; padding: 0; }
  html, body {
    width: 1200px; height: 960px; overflow: hidden;
    background: var(--backdrop);
  }
  .flyer {
    position: absolute; left: 282px; top: 30px;
    width: 568px; height: 803px;
    transform: scale(1.12); transform-origin: top left;
    background: var(--paper);
    font-family: "PT Sans", Arial, sans-serif;
    color: var(--ink);
    overflow: hidden;
    box-shadow: 0 2px 10px rgba(0,0,0,.12);
  }
  .flyer-shapes { position: absolute; inset: 0; }
  .headline {
    position: absolute;
    font-family: "Raleway", Arial, sans-serif;
    font-weight: 300;
    text-transform: uppercase;
    letter-spacing: .5px;
  }
  .headline strong { font-weight: 700; }
  .headline--left { left: 40px; top: 70px; color: var(--paper); font-size: 20px; line-height: 34px; }
  .headline--right { right: 41px; top: 130px; color: var(--sky); font-size: 19px; line-height: 24px; text-align: right; }
  .headline--right .expertise { font-size: 25px; font-weight: 600; line-height: 34px; }

  .block { position: absolute; font-size: 9px; line-height: 11.5px; width: 215px; }
  .block h3 {
    color: var(--sky); font-size: 8.5px; font-weight: 700;
    text-transform: uppercase; letter-spacing: .2px;
    margin-bottom: 1px;
  }
  .block h3.plain { text-transform: none; }
  .block p + h3, .block ul + h3 { margin-top: 11px; }
  .block .underline { text-decoration: underline; }
  .block ul { list-style: none; margin-top: 2px; }
  .block li { position: relative; padding-left: 14px; }
  .block li::before {
    content: ""; position: absolute; left: 3px; top: 3.5px;
    width: 4px; height: 4px; border-radius: 50%; background: var(--sky);
  }

  .block--who { left: 40px; top: 221px; }
  .block--means { left: 324px; top: 221px; }
  .block--services { left: 40px; top: 520px; }
  .block--principles { left: 330px; top: 520px; width: 210px; }
  .block--principles h3:first-child { margin-left: 3px; }

  .callout {
    position: absolute; left: 74px; top: 654px;
    font-size: 10px; line-height: 11px; font-weight: 700;
    text-transform: uppercase; color: var(--sky);
  }
  .callout span { color: var(--navy); }

  .brand {
    position: absolute; left: 200px; top: 441px;
    display: flex; align-items: center; gap: 7px;
  }
  .brand-square { width: 18px; height: 18px; background: var(--sky); }
  .brand-name {
    font-family: "PT Sans", Arial, sans-serif; font-weight: 700;
    font-size: 25px; color: var(--navy); letter-spacing: -.3px;
  }
</style>
</head>
<body>
  <main class="flyer">
    <svg class="flyer-shapes" width="568" height="803" viewBox="0 0 568 803">
      <rect class="band-sky" x="0" y="0" width="568" height="200" fill="var(--sky)"/>
      <rect class="band-pattern" x="320" y="2" width="245" height="88" fill="var(--sky-soft)" opacity=".55" role="img" aria-label="Rows of small light-blue droplet shapes as a decorative pattern"/>
      <polygon class="band-slate" points="0,162 372,92 568,92 568,402 0,402" fill="var(--slate)"/>
      <rect class="base-mist" x="0" y="512" width="568" height="291" fill="var(--mist)"/>
      <rect class="edge-mist" x="539" y="402" width="29" height="401" fill="var(--mist)"/>
      <rect class="centre-band" x="0" y="402" width="539" height="110" fill="var(--paper)"/>
      <polygon class="panel panel--left" points="18,204 244,204 264,224 264,803 18,803" fill="var(--paper)"/>
      <polygon class="panel panel--right" points="312,204 539,204 539,803 292,803 292,224" fill="var(--paper)"/>
    </svg>

    <h1 class="headline headline--left">You can’t outsource<br>your <strong>risk</strong></h1>
    <h2 class="headline headline--right">But<br>you can insource<br><span class="expertise">Expertise</span></h2>

    <section class="block block--who">
      <h3>Who is Corvin’s Gate?</h3>
      <p>A team of independent, passionate risk advisors with over 200 years combined experience in financial market risk management, funding &amp; debt advisory.</p>
      <h3>What can we do for you?</h3>
      <p>We partner with clients to gain a deep understanding of their needs. We then help them <span class="underline">solve their risk and funding issues by creating and explaining sustainable treasury policy.</span></p>
      <h3 class="plain">Debt Advisory</h3>
      <p>Design &amp; Execution of debt funding strategies.</p>
    </section>

    <section class="block block--means">
      <h3>What it means for our clients</h3>
      <p>Our market experience means our clients receive well considered, completely independent advice and solutions covering:</p>
      <ul>
        <li>Commodities</li>
        <li>Foreign Exchange</li>
        <li>Interest Rates</li>
        <li>Project Finance</li>
        <li>Treasury Software Solutions</li>
        <li>Market Valuations incl. CVA / DVA</li>
        <li>Hedge Effectiveness Testing</li>
        <li>Compliance Reporting</li>
      </ul>
    </section>

    <div class="brand">
      <span class="brand-square"></span>
      <span class="brand-name">Corvin’s Gate</span>
    </div>

    <section class="block block--services">
      <h3 class="plain">Market Risk Advisory</h3>
      <p>Design &amp; Execution of hedging strategies</p>
      <h3 class="plain">Active Engagement</h3>
      <p>Fully engaged risk review, reporting, strategy development and execution enhancement.</p>
      <h3>What is our measure of success?</h3>
      <p>Our only true measure of success is successful, sustainable clients that stand out from their peers.</p>
    </section>

    <p class="callout">Integration of<br><span>Market risk strategy<br>&amp; corporate strategy</span><br>is essential</p>

    <section class="block block--principles">
      <h3>Our principles</h3>
      <ul>
        <li>Aspire to always deliver value to our clients.</li>
        <li>Always provide frank, robust advice.</li>
        <li>Be fierce but commercial client advocates.</li>
      </ul>
      <h3>What’s our philosophy?</h3>
      <p>Markets are dynamic, so proper Risk Management must also be a dynamic and on-going process. Risk Management is not about “beating the market”, its about “not taking a beating” from adverse market conditions.</p>
      <p style="margin-top:11px">When your bottom line is exposed to volatile markets, appropriate preparation is the key to a sustainable business. We help our clients to integrate their risk management objectives with their overall corporate strategy.</p>
    </section>
  </main>
</body>
</html>
```